Fat Loss Specialist Personal Training

I need a flyer which is of a high professional standard and looks to the customer that it represents my business as a quality company. I am a personal trainer who specialises in Fat Loss and want this to be the main focus of the flyer. My business is called Summit Sculpt. Please have a look at my website to see what I offer - www.summit-sculpt.co.uk . On the flyer I want it to show what I offer such as one to one PT, nutrition plans etc. A5 Size Flyer.

Target Market(s)

Women

Industry/Entity Type

Business

Font styles to use
Other font styles liked:
• Arial

Requirements
Must have
• Personal Training
• Fat Loss Specialist
• Summit Sculpt Logo on it (my business)
• My details needs to be on it -
• Contact number - 07493021568
• Email - dan@summit-sculpt.co.uk
Nice to have
• Motivating to the customer
• Well presented
• High quality flyer
• Friendly approach
• Follow the same colour scheme as my website
Should not have
• No swear words
• No blurry images / texts

```html
<!DOCTYPE html>
<html lang="en">
<head>
<meta charset="utf-8">
<title>Summit Sculpt – Fat Loss Specialist Personal Training</title>
<link rel="stylesheet" href="https://fonts.googleapis.com/css2?family=Arimo:ital,wght@0,400;0,700;1,400;1,700&family=Bebas+Neue&display=swap">
<style>
  :root {
    --ink: #1f1f21;
    --ink-soft: #3a3a3d;
    --panel: #5b5c60;
    --sky: #64c8ee;
    --sky-deep: #1e6a93;
    --white: #ffffff;
    --bg-top: #f6f7f8;
    --bg-bottom: #dde0e4;
    --skin-light: #efd5c4;
    --skin-mid: #ddb59d;
  }
  * { box-sizing: border-box; margin: 0; padding: 0; }
  html, body { width: 845px; height: 1200px; overflow: hidden; background: #ffffff; }
  .flyer {
    position: relative; width: 845px; height: 1200px; overflow: hidden;
    font-family: "Arimo", Arial, sans-serif; color: var(--ink);
  }
  .backdrop { position: absolute; inset: 0; }
  .abs { position: absolute; }

  .brand-name { left: 30px; top: 68px; font-size: 50px; font-weight: 400; color: var(--ink-soft); letter-spacing: -1px; }
  .brand-tagline { left: 200px; top: 130px; font-size: 14px; font-style: italic; color: var(--ink-soft); }
  .brand-tagline b { color: var(--ink); }

  .hero { left: 46px; top: 194px; }
  .hero-lead { font-size: 40px; font-weight: 700; line-height: 1.05; color: var(--ink); }
  .hero-sub { font-size: 26px; line-height: 1.2; color: var(--ink-soft); }
  .hero-goal { margin-top: 26px; font-size: 26px; line-height: 1.25; color: var(--ink-soft); }
  .hero-goal b { color: var(--ink); }
  .hero-cta { margin: 4px 0 0 190px; font-size: 34px; font-weight: 700; color: var(--sky-deep); }

  .offer { color: var(--white); }
  .offer-title { font-family: "Bebas Neue", "Arial Narrow", sans-serif; font-size: 44px; line-height: 1; color: var(--sky); letter-spacing: 0.5px; }
  .offer-sub { font-size: 19px; font-style: italic; line-height: 1.2; margin-top: 2px; }
  .offer-intro { font-size: 19px; font-weight: 700; line-height: 1.22; }
  .checks { list-style: none; margin-top: 4px; }
  .checks li { font-size: 22px; line-height: 31px; padding-left: 32px; position: relative; }
  .checks li svg { position: absolute; left: 8px; top: 10px; }
  .perks { list-style: none; }
  .perks li { font-size: 18px; font-weight: 700; line-height: 29px; padding-left: 30px; position: relative; }
  .perks li svg { position: absolute; left: 8px; top: 9px; }
  .perks .note { font-weight: 400; font-style: italic; font-size: 16px; line-height: 19px; display: block; padding-left: 0; }

  .online { left: 58px; top: 534px; width: 340px; }
  .online .offer-intro { margin-top: 28px; }
  .online .perks { margin-top: 34px; }
  .signup { left: 58px; top: 1030px; }
  .signup-label { font-size: 24px; font-weight: 700; color: var(--sky); }
  .signup-url { font-size: 26px; font-weight: 700; color: var(--white); margin-top: 6px; }

  .training { left: 490px; top: 696px; width: 330px; }
  .training .offer-intro { margin-top: 32px; }
  .training .perks { margin-top: 26px; }

  .contact-bar { left: 0; top: 1140px; width: 845px; height: 60px; background: var(--white); }
  .contact-email { left: 46px; top: 19px; font-size: 18px; font-weight: 700; color: var(--ink); display: flex; align-items: center; gap: 12px; }
  .contact-phone { left: 484px; top: 10px; font-size: 33px; font-weight: 700; color: var(--ink); letter-spacing: 2px; display: flex; align-items: center; gap: 14px; }
  .contact-divider { left: 422px; top: 10px; width: 2px; height: 40px; background: var(--ink-soft); }
</style>
</head>
<body>
<div class="flyer">
  <svg class="backdrop" width="845" height="1200" viewBox="0 0 845 1200" aria-hidden="true">
    <defs>
      <linearGradient id="bgGrad" x1="0" y1="0" x2="0" y2="1">
        <stop offset="0" stop-color="var(--bg-top)"/>
        <stop offset="1" stop-color="var(--bg-bottom)"/>
      </linearGradient>
      <linearGradient id="heroGrad" x1="0" y1="0" x2="1" y2="1">
        <stop offset="0" stop-color="var(--skin-light)"/>
        <stop offset="1" stop-color="var(--skin-mid)"/>
      </linearGradient>
    </defs>
    <rect width="845" height="1200" fill="url(#bgGrad)"/>
    <path d="M0,432 C150,380 310,446 480,432 C620,420 730,380 845,352 L845,560 L0,560 Z" fill="var(--sky)"/>
    <path d="M0,516 C160,490 330,470 520,500 C650,520 760,522 845,500 L845,1140 L0,1140 Z" fill="var(--panel)"/>
    <path d="M470,0 L845,0 L845,620 C760,662 640,640 566,560 C505,480 476,300 470,0 Z" fill="url(#heroGrad)" role="img" aria-label="Photo of a slim woman in white sportswear measuring her waist with a tape measure"/>
    <line x1="422" y1="618" x2="422" y2="1002" stroke="var(--sky)" stroke-width="2"/>
  </svg>

  <div class="abs brand-name">SummitSculpt</div>
  <div class="abs brand-tagline">Fat Loss Specialist <b>Personal Training</b></div>

  <div class="abs hero">
    <div class="hero-lead">Fat Loss</div>
    <div class="hero-sub">Muscle Gain,<br>Health and Performance...</div>
    <div class="hero-goal">Whatever the goal,<br>earn your <b>Summit Sculpt</b></div>
    <div class="hero-cta">TODAY!</div>
  </div>

  <section class="abs offer online">
    <h2 class="offer-title">Online Membership</h2>
    <p class="offer-sub">Online coaching, right at the<br>hands of your computer</p>
    <p class="offer-intro">It doesnt get easier than<br>online membership -</p>
    <ul class="checks">
      <li><svg width="14" height="12" viewBox="0 0 14 12"><path d="M1,6 L5,10 L13,1" fill="none" stroke="var(--sky)" stroke-width="2.5"/></svg>100% attention,</li>
      <li><svg width="14" height="12" viewBox="0 0 14 12"><path d="M1,6 L5,10 L13,1" fill="none" stroke="var(--sky)" stroke-width="2.5"/></svg>100% passion,</li>
      <li><svg width="14" height="12" viewBox="0 0 14 12"><path d="M1,6 L5,10 L13,1" fill="none" stroke="var(--sky)" stroke-width="2.5"/></svg>100% commitment,</li>
      <li><svg width="14" height="12" viewBox="0 0 14 12"><path d="M1,6 L5,10 L13,1" fill="none" stroke="var(--sky)" stroke-width="2.5"/></svg>100% Summit Sculpt</li>
    </ul>
    <ul class="perks">
      <li><svg width="11" height="11" viewBox="0 0 11 11"><path d="M0,0 L11,5.5 L0,11 L3,5.5 Z" fill="var(--white)"/></svg>Meal Plans</li>
      <li><svg width="11" height="11" viewBox="0 0 11 11"><path d="M0,0 L11,5.5 L0,11 L3,5.5 Z" fill="var(--white)"/></svg>Supplement Guides</li>
      <li><svg width="11" height="11" viewBox="0 0 11 11"><path d="M0,0 L11,5.5 L0,11 L3,5.5 Z" fill="var(--white)"/></svg>Online Workouts</li>
      <li><svg width="11" height="11" viewBox="0 0 11 11"><path d="M0,0 L11,5.5 L0,11 L3,5.5 Z" fill="var(--white)"/></svg>Personalised Gym Programmes</li>
    </ul>
  </section>

  <div class="abs signup">
    <div class="signup-label">SIGN UP TODAY</div>
    <div class="signup-url">www.summit-sculpt.co.uk</div>
  </div>

  <section class="abs offer training">
    <h2 class="offer-title">Personal Training</h2>
    <p class="offer-sub">Effective Results in Efficent Time</p>
    <p class="offer-intro">One to One- If you have a goal,<br>we can achieve it.</p>
    <ul class="checks">
      <li><svg width="14" height="12" viewBox="0 0 14 12"><path d="M1,6 L5,10 L13,1" fill="none" stroke="var(--sky)" stroke-width="2.5"/></svg>100% attention,</li>
      <li><svg width="14" height="12" viewBox="0 0 14 12"><path d="M1,6 L5,10 L13,1" fill="none" stroke="var(--sky)" stroke-width="2.5"/></svg>100% passion,</li>
      <li><svg width="14" height="12" viewBox="0 0 14 12"><path d="M1,6 L5,10 L13,1" fill="none" stroke="var(--sky)" stroke-width="2.5"/></svg>100% commitment,</li>
      <li><svg width="14" height="12" viewBox="0 0 14 12"><path d="M1,6 L5,10 L13,1" fill="none" stroke="var(--sky)" stroke-width="2.5"/></svg>100% Summit Sculpt</li>
    </ul>
    <ul class="perks">
      <li><svg width="11" height="11" viewBox="0 0 11 11"><path d="M0,0 L11,5.5 L0,11 L3,5.5 Z" fill="var(--white)"/></svg>Meal Plans</li>
      <li><svg width="11" height="11" viewBox="0 0 11 11"><path d="M0,0 L11,5.5 L0,11 L3,5.5 Z" fill="var(--white)"/></svg>Supplement Guides</li>
      <li><svg width="11" height="11" viewBox="0 0 11 11"><path d="M0,0 L11,5.5 L0,11 L3,5.5 Z" fill="var(--white)"/></svg>Discounted Memberships
        <span class="note">all inclusive of our Personal<br>Training Package.</span></li>
    </ul>
  </section>

  <footer class="abs contact-bar">
    <div class="abs contact-email">
      <svg width="22" height="15" viewBox="0 0 22 15" aria-hidden="true"><rect width="22" height="15" fill="var(--ink-soft)"/><path d="M0,0 L11,8 L22,0" fill="none" stroke="var(--white)" stroke-width="1.5"/></svg>
      dan@summit-sculpt.co.uk
    </div>
    <div class="abs contact-divider"></div>
    <div class="abs contact-phone">
      <svg width="34" height="28" viewBox="0 0 34 28" aria-hidden="true"><path d="M2,9 C2,3 32,3 32,9 L32,12 L25,12 L25,8 L9,8 L9,12 L2,12 Z" fill="var(--ink)"/><path d="M7,13 L27,13 L31,27 L3,27 Z" fill="var(--ink)"/><circle cx="17" cy="20" r="3.5" fill="var(--white)"/></svg>
      07493021568
    </div>
  </footer>
</div>
</body>
</html>
```